KLV Business Card - Courier/Transportation - Needs Double Sided Business Card

I am searching for business cards for my company. Currently I just need cards for the (3) founders.

We are a new courier/transporation company that specializes in the medical/pharmaceutical arena.

As you will see from our logo, our primary colors are green and black. We strive to have an efficient, streamlined service offering. I like traditional looks, but also want to showcase our young, modern feel. I would like our card to be double sided.

Target Market(s)

Pharmacies
Hospitals
Physcian Office
Labs

Industry/Entity Type

Business

```html
<!DOCTYPE html>
<html lang="en">
<head>
<meta charset="utf-8">
<title>KLV Courier Business Card</title>
<link rel="stylesheet" href="https://fonts.googleapis.com/css2?family=Fira+Sans:wght@600;700&display=swap">
<style>
  :root {
    --backdrop: #9fbcb0;
    --card: #f1f1f0;
    --ink: #1c1c1c;
    --brand-green: #2e9a3c;
    --edge-green: #3a8f35;
  }
  * { margin: 0; padding: 0; box-sizing: border-box; }
  html, body {
    width: 1200px;
    height: 1000px;
    overflow: hidden;
    background: var(--backdrop);
  }
  .canvas {
    position: relative;
    width: 1200px;
    height: 1000px;
  }
  .business-card {
    position: absolute;
    left: 160px;
    top: 245px;
    width: 880px;
    height: 510px;
    background: var(--card);
    border-bottom: 6px solid var(--edge-green);
    box-shadow: 0 10px 30px rgba(0, 0, 0, 0.18);
    font-family: "Fira Sans", Arial, sans-serif;
    color: var(--ink);
  }
  .brand {
    position: absolute;
    left: 70px;
    top: 60px;
    display: flex;
    align-items: center;
    gap: 14px;
  }
  .brand-square {
    width: 30px;
    height: 30px;
    background: var(--brand-green);
  }
  .brand-name {
    font-size: 44px;
    font-weight: 700;
    letter-spacing: 1px;
    color: var(--brand-green);
  }
  .contact-block {
    position: absolute;
    left: 70px;
    top: 170px;
    font-size: 21px;
    font-weight: 600;
    line-height: 1.3;
  }
  .contact-block .identity { margin-bottom: 20px; }
</style>
</head>
<body>
  <main class="canvas">
    <section class="business-card" aria-label="KLV Courier business card">
      <header class="brand">
        <span class="brand-square" aria-hidden="true"></span>
        <span class="brand-name">KLV Courier</span>
      </header>
      <div class="contact-block">
        <div class="identity">
          <p class="company">KLV Courier</p>
          <p class="job-title">Job Title</p>
        </div>
        <p class="address">2240 Maple Ridge Dr, Carmel, IN 46032</p>
        <p class="phone">Phone</p>
        <p class="website">www.KLVcourier.net</p>
        <p class="email">mail@KLVcourier.net</p>
      </div>
    </section>
  </main>
</body>
</html>
```